Wageline Associates Business Card Design

We need a business card designed around our new logo. The business card should be modern in design & should communicate success, confidence, power, sophistication. The target market is young business professionals. This is for a human resource & payroll outsourcing business.

```html
<!DOCTYPE html>
<html lang="en">
<head>
<meta charset="utf-8">
<title>Wageline Associates Business Card</title>
<link rel="stylesheet" href="https://fonts.googleapis.com/css2?family=Playfair+Display:ital,wght@0,400;0,500;1,400&display=swap">
<style>
  :root {
    --page-bg: #e9e6e2;
    --card-black: #0b0b0b;
    --brand-red: #e8000b;
    --brand-red-deep: #c90008;
    --text-white: #ffffff;
    --text-soft: #f2f2f2;
  }
  * { box-sizing: border-box; margin: 0; padding: 0; }
  html, body {
    width: 1200px;
    height: 900px;
    overflow: hidden;
    background: var(--page-bg);
  }
  .card {
    position: absolute;
    left: 120px;
    top: 154px;
    width: 960px;
    height: 592px;
    background: var(--card-black);
    overflow: hidden;
    box-shadow: 0 10px 30px rgba(0,0,0,0.18);
    font-family: "Playfair Display", Georgia, serif;
    color: var(--text-white);
  }
  .card-art {
    position: absolute;
    inset: 0;
    width: 100%;
    height: 100%;
  }
  .brand {
    position: absolute;
    left: 58px;
    top: 70px;
    color: var(--text-white);
    font-weight: 400;
    line-height: 1;
  }
  .brand-name {
    display: block;
    font-size: 76px;
    letter-spacing: -0.5px;
  }
  .brand-sub {
    display: block;
    font-size: 29px;
    letter-spacing: 3px;
    margin-top: 6px;
    padding-left: 118px;
  }
  .person {
    position: absolute;
    left: 58px;
    top: 230px;
  }
  .person-name {
    font-style: italic;
    font-size: 36px;
    color: var(--brand-red);
    line-height: 1.1;
  }
  .person-role {
    font-style: italic;
    font-size: 26px;
    color: var(--text-soft);
    margin-top: 4px;
  }
  .contact-list {
    position: absolute;
    left: 58px;
    top: 350px;
    list-style: none;
  }
  .contact-item {
    display: flex;
    align-items: center;
    font-style: italic;
    font-size: 25px;
    line-height: 34px;
    color: var(--text-soft);
  }
  .contact-icon {
    width: 19px;
    height: 19px;
    margin-right: 9px;
    fill: var(--brand-red);
    flex: none;
  }
  .address {
    position: absolute;
    left: 58px;
    top: 490px;
    font-style: italic;
    font-size: 25px;
    line-height: 34px;
    color: var(--text-soft);
  }
</style>
</head>
<body>
  <article class="card">
    <svg class="card-art" viewBox="0 0 960 592" aria-hidden="true">
      <defs>
        <linearGradient id="red-band" x1="0" y1="0" x2="0" y2="1">
          <stop offset="0" stop-color="var(--brand-red)"/>
          <stop offset="1" stop-color="var(--brand-red-deep)"/>
        </linearGradient>
      </defs>
      <path d="M826 0 H960 V592 H488 C700 470 800 260 826 0 Z" fill="url(#red-band)"/>
    </svg>

    <div class="brand">
      <span class="brand-name">Wageline</span>
      <span class="brand-sub">Associates</span>
    </div>

    <div class="person">
      <p class="person-name">Daniel Marsh</p>
      <p class="person-role">Managing Director</p>
    </div>

    <ul class="contact-list">
      <li class="contact-item">
        <svg class="contact-icon" viewBox="0 0 20 20"><path d="M3 7c0-2 3-4 7-4s7 2 7 4v2h-4V7.5C12 7 11 6.8 10 6.8S8 7 7 7.5V9H3z M5 10h10l2 6H3z"/></svg>
        044-987 650 312
      </li>
      <li class="contact-item">
        <svg class="contact-icon" viewBox="0 0 20 20"><path d="M6 1h8a1 1 0 0 1 1 1v16a1 1 0 0 1-1 1H6a1 1 0 0 1-1-1V2a1 1 0 0 1 1-1zm1 2v12h6V3zm3 13.2a1 1 0 1 0 0 1.6 1 1 0 0 0 0-1.6z"/></svg>
        044-987 650 312
      </li>
      <li class="contact-item">
        <svg class="contact-icon" viewBox="0 0 20 20"><path d="M2 4h16v12H2z M3 5l7 6 7-6" stroke="#0b0b0b" stroke-width="1.2"/></svg>
        hello@wagelineco.com
      </li>
      <li class="contact-item">
        <svg class="contact-icon" viewBox="0 0 20 20"><circle cx="10" cy="10" r="8"/><path d="M2 10h16M10 2c3 3 3 13 0 16M10 2c-3 3-3 13 0 16" stroke="#0b0b0b" stroke-width="1" fill="none"/></svg>
        www.wagelineco.com
      </li>
    </ul>

    <p class="address">48 Harbour Row, Suite 9<br>Eastport, 204518</p>
  </article>
</body>
</html>
```